Business Card Design Project

We're an orthopaedic office, and our colors are blue white and balck. Dealing with physicians and healthcare execs, I'd like this card to have a classy, yet overpowering wow factor.

Here are a couple of cards I like that are close to what I'm looking for:
http://www.pixelbazaro.com/design/392047
http://www.pixelbazaro.com/design/286390

Industry/Entity Type

Healthcare

```html
<!DOCTYPE html>
<html lang="en">
<head>
<meta charset="utf-8">
<title>Crestline Orthopaedic – Business Card</title>
<link rel="stylesheet" href="https://fonts.googleapis.com/css2?family=Exo+2:wght@300;400;600&display=swap">
<style>
  :root {
    --brand-blue: #0a67b2;
    --card-white: #f7f7f7;
    --ink: #1d1d1d;
    --stage: #d9d9d9;
  }
  * { margin: 0; padding: 0; box-sizing: border-box; }
  html, body {
    width: 1200px; height: 900px; overflow: hidden;
    background: var(--stage);
    font-family: "Exo 2", sans-serif;
  }
  .card {
    position: absolute;
    box-shadow: 0 10px 28px rgba(0,0,0,.28);
  }
  .card-back {
    left: 380px; top: 70px;
    width: 580px; height: 331px;
    background: var(--brand-blue);
    display: flex; align-items: center; justify-content: center;
  }
  .back-name {
    color: #fff;
    font-weight: 600;
    font-size: 46px;
    letter-spacing: 4px;
    display: flex; align-items: center; gap: 18px;
  }
  .back-name .mark-square {
    width: 34px; height: 34px; background: #fff;
  }
  .card-front {
    left: 140px; top: 450px;
    width: 700px; height: 400px;
    background: var(--card-white);
    color: var(--ink);
  }
  .brand {
    position: absolute; left: 44px; top: 42px;
    display: flex; align-items: center; gap: 16px;
  }
  .brand .mark-square {
    width: 58px; height: 58px; background: var(--brand-blue);
  }
  .brand-name {
    font-weight: 400; font-size: 34px; letter-spacing: 1px;
    color: var(--ink); line-height: 1;
  }
  .brand-sub {
    font-weight: 300; font-size: 13px; color: var(--ink);
    margin-top: 4px; line-height: 1.15;
  }
  .person {
    position: absolute; left: 44px; top: 178px;
    font-weight: 400; font-size: 27px; letter-spacing: 1.5px;
  }
  .contact {
    position: absolute; left: 44px; top: 236px;
    font-weight: 300; font-size: 19px; line-height: 30px; letter-spacing: .5px;
  }
  .contact .label { color: var(--brand-blue); display: inline-block; width: 24px; padding-left: 6px; }
  .website {
    position: absolute; right: 44px; bottom: 40px;
    color: var(--brand-blue); font-weight: 600; font-size: 19px; letter-spacing: 1px;
  }
</style>
</head>
<body>
  <section class="card card-back">
    <div class="back-name"><span class="mark-square"></span>CRESTLINE</div>
  </section>

  <section class="card card-front">
    <div class="brand">
      <span class="mark-square"></span>
      <div>
        <div class="brand-name">CRESTLINE</div>
        <div class="brand-sub">Orthopaedic &amp; Sports<br>Medicine Center</div>
      </div>
    </div>
    <div class="person">DALTON REEVES | CEO</div>
    <div class="contact">
      <div><span class="label">t</span>(318) 555-0142</div>
      <div><span class="label">e</span>dreeves@crestlineortho.com</div>
      <div>1275 Harlow Ave., Pinedale, LA 71308</div>
    </div>
    <div class="website">www.crestlineortho.com</div>
  </section>
</body>
</html>
```